Larkspur Ridge Management - Business Cards

I need business cards. My current logo was designed by a designer at this site and I very much like and am happy with the results. I would like a business card that is trendy, unique, current yet professional. I deal with high net worth clients daily

Target Market(s)

Out of state investors looking to get into the rental market in Ohio

Industry/Entity Type

Property Management, Consulting

Contact Information for Business Card

Name, Title (Chief Financial Officer) office phone number (555) 817-3094 website address larkridgemgmt.example

Font styles to use
Sans Serif

Colors
0054AA
0677BA
7BADD7
CADEEF
E8F1F8
0094D4
00A9DD
6FCCEA
C7EBF8
E9F6FB
00AB8E
00BBA5
67D7C9
C6EFE9
E9F9F6

```html
<!DOCTYPE html>
<html lang="en">
<head>
<meta charset="utf-8">
<title>Larkspur Ridge Management – Business Cards</title>
<link rel="stylesheet" href="https://fonts.googleapis.com/css2?family=Montserrat:wght@500;700;800&family=Open+Sans:wght@400;600&display=swap">
<style>
  :root {
    --navy: #0054aa;
    --navy-deep: #003f80;
    --accent: #00ab8e;
    --white: #ffffff;
    --ink: #1d2233;
    --backdrop: #d6d6d6;
    --gray-text: #3a3f4c;
  }
  * { margin: 0; padding: 0; box-sizing: border-box; }
  html, body {
    width: 1200px;
    height: 815px;
    overflow: hidden;
    background: var(--backdrop);
  }
  .sheet {
    position: relative;
    width: 1200px;
    height: 815px;
  }
  .card {
    position: absolute;
    width: 540px;
    height: 310px;
    border-radius: 22px;
    overflow: hidden;
    box-shadow: 0 14px 28px rgba(0, 0, 0, 0.22);
  }

  /* Front */
  .card-front {
    left: 50px;
    top: 95px;
    background: var(--white);
  }
  .card-front .wave {
    position: absolute;
    inset: 0;
    width: 100%;
    height: 100%;
  }
  .brand-front {
    position: absolute;
    right: 30px;
    top: 36px;
    width: 240px;
    text-align: right;
    font-family: "Montserrat", sans-serif;
    font-weight: 800;
    font-size: 21px;
    line-height: 1.15;
    letter-spacing: 0.5px;
    color: var(--navy);
    text-transform: uppercase;
  }
  .brand-front span { display: block; white-space: nowrap; }
  .person {
    position: absolute;
    left: 34px;
    top: 44px;
  }
  .person-name {
    font-family: "Montserrat", sans-serif;
    font-weight: 800;
    font-size: 24px;
    letter-spacing: 0.5px;
    text-transform: uppercase;
    white-space: nowrap;
  }
  .person-name .first { color: var(--accent); }
  .person-name .last { color: var(--navy); }
  .person-title {
    font-family: "Open Sans", sans-serif;
    font-size: 13px;
    color: var(--gray-text);
    margin-top: 2px;
  }
  .divider {
    width: 18px;
    height: 2px;
    background: var(--accent);
    margin: 22px 0 18px;
  }
  .address {
    font-family: "Open Sans", sans-serif;
    font-size: 13px;
    line-height: 1.35;
    color: var(--ink);
    margin-bottom: 6px;
  }
  .contacts { list-style: none; }
  .contacts li {
    display: flex;
    align-items: center;
    gap: 8px;
    font-family: "Open Sans", sans-serif;
    font-size: 13px;
    line-height: 1.55;
    color: var(--ink);
    white-space: nowrap;
  }
  .contacts svg { width: 12px; height: 12px; flex: none; }

  /* Back */
  .card-back {
    left: 610px;
    top: 410px;
    background: var(--navy-deep);
    border-bottom: 4px solid var(--accent);
    display: flex;
    align-items: center;
    justify-content: center;
  }
  .brand-back {
    font-family: "Montserrat", sans-serif;
    font-weight: 800;
    font-size: 40px;
    line-height: 1.1;
    color: var(--white);
    text-align: center;
    text-transform: uppercase;
    letter-spacing: 1px;
  }
</style>
</head>
<body>
<main class="sheet">

  <section class="card card-front" aria-label="Business card front">
    <svg class="wave" viewBox="0 0 540 310" preserveAspectRatio="none" aria-hidden="true">
      <path d="M0,302 C190,304 300,250 390,195 C440,165 490,148 540,142 L540,152 C490,158 445,175 398,203 C310,256 190,310 0,310 Z" fill="var(--accent)"/>
      <path d="M0,310 C190,310 310,256 398,203 C445,175 490,158 540,152 L540,310 Z" fill="var(--navy-deep)"/>
    </svg>

    <div class="brand-front"><span>Larkspur Ridge</span><span>Management</span></div>

    <div class="person">
      <h1 class="person-name"><span class="first">Dana</span> <span class="last">Whitfield</span></h1>
      <p class="person-title">Chief Financial Officer</p>
      <div class="divider"></div>
      <p class="address">418 Alder Lane,<br>2210 Columbus, OH 43215</p>
      <ul class="contacts">
        <li>
          <svg viewBox="0 0 12 12" aria-hidden="true"><path d="M2.5 1 L4.5 1 L5.2 3.4 L4 4.4 C4.6 5.8 6 7.2 7.6 8 L8.6 6.8 L11 7.5 L11 9.5 C11 10.3 10.3 11 9.5 11 C5 11 1 7 1 2.5 C1 1.7 1.7 1 2.5 1 Z" fill="var(--accent)"/></svg>
          +1 (555) 817-3094
        </li>
        <li>
          <svg viewBox="0 0 12 12" aria-hidden="true"><rect x="1" y="2.5" width="10" height="7" rx="1" fill="var(--accent)"/><path d="M1.5 3 L6 6.5 L10.5 3" stroke="var(--white)" stroke-width="1" fill="none"/></svg>
          info@larkridgemgmt.example
        </li>
        <li>
          <svg viewBox="0 0 12 12" aria-hidden="true"><circle cx="6" cy="6" r="5" fill="var(--accent)"/><path d="M1 6 H11 M6 1 C3.5 3.5 3.5 8.5 6 11 M6 1 C8.5 3.5 8.5 8.5 6 11" stroke="var(--white)" stroke-width="0.8" fill="none"/></svg>
          www.larkridgemgmt.example
        </li>
      </ul>
    </div>
  </section>

  <section class="card card-back" aria-label="Business card back">
    <div class="brand-back">Larkspur Ridge<br>Management</div>
  </section>

</main>
</body>
</html>
```